Worksheet for a seminar - Circle of Balance

I need a 1 page worksheet for a course I am running next week.
1. The worksheet is based is designed to tie into Dorvelle who use 4 colours per specific quadrants - Blue top left, Yellow top right, Green bottom left, Red bottom right. As this is designed to be written and to be printed, it may need to be pale colours however I am open to the correct colours with the image on top if necessary

2. The wellbeing wheel needs to be a design of it's own as it will be used in other things. I would like to have a format for the base wheel that can be changed by me (Only the title names)

3. I have provided the 2 business logo's - these down need to be too big

I hope this helps.

Corporate managers and staff - worksheet being used in a workshop

Wheel

• A professional looking wheel that can be used for other purposes. I want to be able to change the 'pie' titles. I will also require a A4 size of the wheel with blank spaces for titles
• A modern feel

```html
<!DOCTYPE html>
<html lang="en">
<head>
<meta charset="utf-8">
<title>Circle of Balance – Worksheet</title>
<link rel="stylesheet" href="https://fonts.googleapis.com/css2?family=Arvo:wght@400;700&family=Open+Sans:wght@400;600;700&display=swap">
<style>
  :root{
    --page-bg:#e6e6e6;
    --sheet:#ffffff;
    --ink:#1d1d1d;
    --title-blue:#0b6fb8;
    --title-plum:#9c1a6e;
    --goal-pink:#e3245c;
    --ring-dark:#2f2f2f;
    --row-light:#f0f0f0;
    --row-mid:#d8d8d8;
    --row-line:#8f8f8f;
    --when-deep:#0a6fb8;
    --when-bright:#0cbedc;
    --brand-green:#63b02d;
    --brand-teal:#3db597;
    --foot-band:#f6dc5c;
    --slab:"Arvo", serif;
    --sans:"Open Sans", sans-serif;
  }
  *{box-sizing:border-box;margin:0;padding:0}
  html,body{width:1200px;height:1200px;overflow:hidden}
  body{background:var(--page-bg);position:relative;font-family:var(--sans);color:var(--ink)}
  .sheet{position:absolute;left:179px;top:10px;width:972px;height:1362px;background:var(--sheet);
         transform:scale(.8664);transform-origin:0 0;box-shadow:0 2px 10px rgba(0,0,0,.18);overflow:hidden}
  .abs{position:absolute}
  .brand-top{left:340px;top:50px;display:flex;align-items:center;gap:12px;font-family:var(--slab);font-size:24px;color:#555}
  .brand-dot{width:34px;height:34px;border-radius:50%;background:var(--title-blue)}
  .title{left:0;width:100%;text-align:center;font-family:var(--slab);font-weight:700}
  .title-main{top:122px;font-size:36px;color:var(--title-blue)}
  .title-sub{top:160px;font-size:29px;color:var(--title-plum)}
  .step{font-family:var(--slab);font-size:28px}
  .step b{font-size:32px}
  .step-assess{left:73px;top:220px;color:var(--title-blue)}
  .step-goals{left:565px;top:220px;color:var(--goal-pink)}
  .step-q{font-family:var(--slab);font-size:18px;color:var(--ink)}
  .q-assess{left:107px;top:255px}
  .q-goals{left:602px;top:255px}
  .wheel{width:440px;height:440px;top:284px}
  .wheel-assess{left:40px}
  .wheel-goals{left:502px}
  .date-line{font-family:var(--slab);font-weight:700;font-size:17px;top:730px;display:flex;align-items:flex-end}
  .date-line span.fill{display:inline-block;border-bottom:2px dotted #333;margin-left:8px;height:16px}
  .date-now{left:45px}
  .date-now .fill{width:268px}
  .date-goal{left:524px}
  .date-goal .fill{width:198px}
  .section-head{font-family:var(--slab);font-size:34px;color:var(--title-plum);top:762px}
  .head-action{left:45px}
  .head-reflect{left:527px}
  .col-head{font-family:var(--slab);font-size:18px;top:816px}
  .col-action{left:162px}
  .col-when{left:360px}
  .action-plan{left:40px;top:852px;width:400px}
  .action-row{position:relative;height:87px;border:1.5px solid var(--row-line);border-radius:8px}
  .action-row:nth-child(odd){background:var(--row-light)}
  .action-row:nth-child(even){background:var(--row-mid)}
  .action-when{position:absolute;right:-1px;top:3px;bottom:3px;width:109px;border-radius:8px}
  .action-row:nth-child(odd) .action-when{background:var(--when-deep)}
  .action-row:nth-child(even) .action-when{background:var(--when-bright)}
  .reflect-q{left:529px;font-family:var(--slab);font-size:15px;line-height:19px;width:400px}
  .reflect-box{left:526px;width:401px;height:66px;background:var(--row-light);border:1.5px solid var(--row-line);border-radius:8px}
  .partner{display:flex;align-items:center;gap:10px;font-family:var(--slab);font-weight:700;font-size:24px;top:1262px;white-space:nowrap}
  .partner-left{left:112px;color:var(--brand-green)}
  .partner-right{left:618px;color:var(--brand-teal)}
  .partner i{display:block;width:22px;height:22px;border-radius:50%;background:currentColor;flex:none}
  .foot-band{left:0;bottom:0;width:100%;height:20px;background:var(--foot-band)}
  svg text{font-family:var(--sans)}
</style>
</head>
<body>
<main class="sheet">
  <div class="abs brand-top"><span class="brand-dot"></span>Brightwheel Wellness</div>

  <h1 class="abs title title-main">CIRCLE OF BALANCE</h1>
  <h2 class="abs title title-sub">A WHOLE BRAIN APPROACH</h2>

  <div class="abs step step-assess"><b>1.</b> ASSESS</div>
  <div class="abs step-q q-assess">Where are you now?</div>
  <div class="abs step step-goals"><b>3.</b> OUT COMES GOALS</div>
  <div class="abs step-q q-goals">where do you want to be ?</div>

  <svg class="abs wheel wheel-assess" viewBox="-220 -220 440 440" aria-label="Wellbeing assessment wheel">
    <defs>
      <g id="scale" stroke="#333" stroke-width="1">
        <path d="M0 -106V-186M-4 -110H4M-4 -118H4M-4 -126H4M-4 -134H4M-6 -142H6M-4 -150H4M-4 -158H4M-4 -166H4M-4 -174H4M-6 -182H6"/>
      </g>
      <path id="seg" d="M-34.2 -94L-65 -178.5A190 190 0 0 1 65 -178.5L34.2 -94A100 100 0 0 0 -34.2 -94Z"/>
      <path id="band" d="M-71.2 -176.2L-79.4 -196.6A212 212 0 0 1 79.4 -196.6L71.2 -176.2A190 190 0 0 0 -71.2 -176.2Z"/>
      <linearGradient id="gYellow" gradientUnits="userSpaceOnUse" x1="0" y1="-100" x2="0" y2="-190"><stop offset="0" stop-color="#fff3c4"/><stop offset="1" stop-color="#fdd85a"/></linearGradient>
      <linearGradient id="gGreen" gradientUnits="userSpaceOnUse" x1="0" y1="-100" x2="0" y2="-190"><stop offset="0" stop-color="#e3f2c6"/><stop offset="1" stop-color="#9dd452"/></linearGradient>
      <linearGradient id="gOrange" gradientUnits="userSpaceOnUse" x1="0" y1="-100" x2="0" y2="-190"><stop offset="0" stop-color="#fbd0bc"/><stop offset="1" stop-color="#f4703f"/></linearGradient>
      <linearGradient id="gTeal" gradientUnits="userSpaceOnUse" x1="0" y1="-100" x2="0" y2="-190"><stop offset="0" stop-color="#c5e6d3"/><stop offset="1" stop-color="#4aab79"/></linearGradient>
      <linearGradient id="gRed" gradientUnits="userSpaceOnUse" x1="0" y1="-100" x2="0" y2="-190"><stop offset="0" stop-color="#f5c5c8"/><stop offset="1" stop-color="#de4a56"/></linearGradient>
      <linearGradient id="gPurple" gradientUnits="userSpaceOnUse" x1="0" y1="-100" x2="0" y2="-190"><stop offset="0" stop-color="#e6c5e1"/><stop offset="1" stop-color="#ad4ca2"/></linearGradient>
      <linearGradient id="gTan" gradientUnits="userSpaceOnUse" x1="0" y1="-100" x2="0" y2="-190"><stop offset="0" stop-color="#e8d8c6"/><stop offset="1" stop-color="#ad8762"/></linearGradient>
      <linearGradient id="gBlue" gradientUnits="userSpaceOnUse" x1="0" y1="-100" x2="0" y2="-190"><stop offset="0" stop-color="#c7e5fb"/><stop offset="1" stop-color="#3aa6f2"/></linearGradient>
      <radialGradient id="hub"><stop offset=".7" stop-color="#f4f4f4"/><stop offset="1" stop-color="#bdbdbd"/></radialGradient>
      <g id="hub-disc">
        <circle r="100" fill="#c9c9c9"/>
        <circle r="92" fill="url(#hub)"/>
        <circle r="76" fill="#e2e2e2"/>
        <circle r="55" fill="#cfcfcf"/>
      </g>
    </defs>
    <circle r="180" fill="var(--ring-dark)"/>

    <g class="segment">
      <use href="#seg" fill="url(#gYellow)"/><use href="#band" fill="#f6c21c"/><use href="#scale"/>
      <text x="-12" y="-138" font-size="11">5</text><text x="-20" y="-186" font-size="11">10</text>
      <text y="-197" font-size="10" font-weight="600" text-anchor="middle" fill="#333">Business Career Study</text>
    </g>
    <g class="segment" transform="rotate(45)">
      <use href="#seg" fill="url(#gGreen)"/><use href="#band" fill="#7cc242"/><use href="#scale"/>
      <text x="-12" y="-138" font-size="11">5</text><text x="-20" y="-170" font-size="11">10</text>
      <text y="-197" font-size="10" font-weight="600" text-anchor="middle" fill="#333">Physical health</text>
    </g>
    <g class="segment" transform="rotate(90)">
      <use href="#seg" fill="url(#gOrange)"/><use href="#band" fill="#f1592a"/><use href="#scale"/>
      <text x="-12" y="-138" font-size="11">5</text><text x="-20" y="-170" font-size="11">10</text>
      <text y="-197" font-size="10" font-weight="600" text-anchor="middle" fill="#fff">Emotional health</text>
    </g>
    <g class="segment" transform="rotate(135)">
      <use href="#seg" fill="url(#gTeal)"/><use href="#band" fill="#0b6b3a"/><use href="#scale"/>
      <text x="-12" y="-138" font-size="11">5</text><text x="-20" y="-170" font-size="11">10</text>
      <text y="-197" font-size="10" font-weight="600" text-anchor="middle" fill="#fff" transform="rotate(180 0 -201)">Spiritual</text>
    </g>
    <g class="segment" transform="rotate(180)">
      <use href="#seg" fill="url(#gRed)"/><use href="#band" fill="#c0282e"/><use href="#scale"/>
      <text x="-12" y="-138" font-size="11">5</text><text x="-20" y="-170" font-size="11">10</text>
      <text y="-197" font-size="10" font-weight="600" text-anchor="middle" fill="#fff" transform="rotate(180 0 -201)">Love relationship</text>
    </g>
    <g class="segment" transform="rotate(225)">
      <use href="#seg" fill="url(#gPurple)"/><use href="#band" fill="#8e1f7e"/><use href="#scale"/>
      <text x="-12" y="-138" font-size="11">5</text><text x="-20" y="-170" font-size="11">10</text>
      <text y="-197" font-size="10" font-weight="600" text-anchor="middle" fill="#fff" transform="rotate(180 0 -201)">Family</text>
    </g>
    <g class="segment" transform="rotate(270)">
      <use href="#seg" fill="url(#gTan)"/><use href="#band" fill="#8a6748"/><use href="#scale"/>
      <text x="-12" y="-138" font-size="11">5</text><text x="-20" y="-170" font-size="11">10</text>
      <text y="-197" font-size="10" font-weight="600" text-anchor="middle" fill="#fff">Social</text>
    </g>
    <g class="segment" transform="rotate(315)">
      <use href="#seg" fill="url(#gBlue)"/><use href="#band" fill="#1b8fd6"/><use href="#scale"/>
      <text x="-12" y="-138" font-size="11">5</text><text x="-20" y="-170" font-size="11">10</text>
      <text y="-197" font-size="10" font-weight="600" text-anchor="middle" fill="#fff">Personal growth</text>
    </g>
    <use href="#hub-disc"/>
  </svg>

  <svg class="abs wheel wheel-goals" viewBox="-220 -220 440 440" aria-label="Whole brain outcome goals wheel">
    <defs>
      <path id="quad" d="M-64.3 -99L-115.5 -177.8A212 212 0 0 1 115.5 -177.8L64.3 -99A118 118 0 0 0 -64.3 -99Z"/>
      <linearGradient id="qBlue" gradientUnits="userSpaceOnUse" x1="-100" y1="0" x2="100" y2="0"><stop offset="0" stop-color="#1590d0"/><stop offset="1" stop-color="#3cc6f5"/></linearGradient>
      <linearGradient id="qYellow" gradientUnits="userSpaceOnUse" x1="-100" y1="0" x2="100" y2="0"><stop offset="0" stop-color="#fdd20a"/><stop offset="1" stop-color="#fff27a"/></linearGradient>
      <linearGradient id="qRed" gradientUnits="userSpaceOnUse" x1="-100" y1="0" x2="100" y2="0"><stop offset="0" stop-color="#ff7566"/><stop offset="1" stop-color="#f0473c"/></linearGradient>
      <linearGradient id="qGreen" gradientUnits="userSpaceOnUse" x1="-100" y1="0" x2="100" y2="0"><stop offset="0" stop-color="#08b04a"/><stop offset="1" stop-color="#86dca0"/></linearGradient>
    </defs>
    <circle r="162" fill="var(--ring-dark)"/>
    <use href="#quad" fill="url(#qBlue)"/>
    <use href="#quad" fill="url(#qYellow)" transform="rotate(90)"/>
    <use href="#quad" fill="url(#qRed)" transform="rotate(180)"/>
    <use href="#quad" fill="url(#qGreen)" transform="rotate(270)"/>
    <use href="#hub-disc"/>
    <g font-size="12" text-anchor="middle" fill="#fff">
      <text y="-178">LOGICAL</text><text y="-163">ANALYTICAL</text><text y="-148">FACT BASED</text><text y="-133">QUANTITATIVE</text>
      <text y="135">INTERPERSONAL</text><text y="150">FEELING BASED</text><text y="165">KINESTHETIC</text><text y="180">EMOTIONAL</text>
    </g>
    <g font-size="12" text-anchor="end" fill="#1d1d1d">
      <text x="-120" y="-22">ORGANIZED</text><text x="-120" y="-7">SEQUENTIAL</text><text x="-120" y="8">PLANNED</text><text x="-120" y="23">DETAILED</text>
    </g>
    <g font-size="12" text-anchor="start" fill="#1d1d1d">
      <text x="120" y="-22">HOLISTIC</text><text x="120" y="-7">INTUITIVE</text><text x="120" y="8">INTEGRATING</text><text x="120" y="23">SYNTHESIZING</text>
    </g>
  </svg>

  <div class="abs date-line date-now">Date:<span class="fill"></span></div>
  <div class="abs date-line date-goal">Date archieved by:<span class="fill"></span></div>

  <h3 class="abs section-head head-action">4. Action plane</h3>
  <h3 class="abs section-head head-reflect">2. Reflect</h3>

  <div class="abs col-head col-action">Action</div>
  <div class="abs col-head col-when">When</div>

  <div class="abs action-plan">
    <div class="action-row"><span class="action-when"></span></div>
    <div class="action-row"><span class="action-when"></span></div>
    <div class="action-row"><span class="action-when"></span></div>
    <div class="action-row"><span class="action-when"></span></div>
  </div>

  <p class="abs reflect-q" style="top:824px">Are there any surprise in you wheel?</p>
  <div class="abs reflect-box" style="top:844px"></div>
  <p class="abs reflect-q" style="top:910px">what wellbeing gaps stad out as being<br>more importent</p>
  <div class="abs reflect-box" style="top:956px"></div>
  <p class="abs reflect-q" style="top:1024px">How do you feel about it?</p>
  <div class="abs reflect-box" style="top:1044px"></div>
  <p class="abs reflect-q" style="top:1110px">How might this affect your personal life / work life&gt;</p>
  <div class="abs reflect-box" style="top:1134px"></div>

  <div class="abs partner partner-left"><i></i>Rise Ahead Coaching</div>
  <div class="abs partner partner-right"><i></i>Steady Desk Health</div>

  <div class="abs foot-band"></div>
</main>
</body>
</html>
```